Need a design for Loan Site with new age design

We need a design for our site www.credvista.in , we deal with different verticals like home loan, personal loan, loan against property and business loans. Feel free to get in touch if you have any questions.

I have like the concept of the drop down on the eye level where consumer is able to select the product they wish and continue with the form https://www.tulsiorbit.com/ . They are in the same line of business as we are.

Here are few more designs which i personally like just to get idea about the taste

https://plumridgestudio.com/
http://zenpik.com/partners

Industry/Entity Type

Loan

Number of Pages Required

2 page

Colors
34a7d7
add136
faa54b
fbee3e

Requirements
Must have
• I have like the concept of the drop down on the eye level where consumer is able to select the product they wish and continue with the form https://www.tulsiorbit.com/ . They are in the same line of business as we are.
• Here are few more designs which i personally like just to get idea about the taste
• https://plumridgestudio.com/
• http://zenpik.com/partners

```html
<!DOCTYPE html>
<html lang="en">
<head>
<meta charset="utf-8">
<title>CredVista – Match Your Loan</title>
<link rel="stylesheet" href="https://fonts.googleapis.com/css2?family=Open+Sans:wght@400;600&display=swap">
<style>
:root{
  --blue:#34a7d7;
  --nav:#1a7fd0;
  --nav-dark:#1466b3;
  --green:#add136;
  --orange:#faa54b;
  --yellow:#fbee3e;
  --ink:#333;
  --foot:#333333;
  --foot-dark:#2a2a2a;
  --white:#fff;
}
*{box-sizing:border-box;margin:0;padding:0}
html,body{width:932px;height:1200px;overflow:hidden}
body{font-family:"Open Sans",Arial,sans-serif;color:var(--ink);background:var(--white);position:relative}
.abs{position:absolute}
/* header */
.site-header{position:absolute;left:0;top:0;width:932px;height:76px;border-top:2px solid var(--blue);background:#fff}
.brand{position:absolute;left:75px;top:26px;display:flex;align-items:center;gap:8px;font-size:18px;font-weight:600;color:var(--nav-dark)}
.brand-mark{width:18px;height:18px;background:var(--nav);border-radius:2px}
.quick{position:absolute;right:78px;top:11px;font-size:12px;color:#444;display:flex;align-items:center;gap:6px}
.quick b{color:var(--nav);font-weight:600}
.nav{position:absolute;left:380px;top:36px;width:552px;height:40px;background:var(--nav);clip-path:polygon(30px 0,100% 0,100% 100%,0 100%)}
.nav-active{position:absolute;left:28px;top:0;width:132px;height:40px;background:var(--nav-dark)}
.nav a{position:absolute;top:0;height:40px;line-height:40px;color:#fff;text-decoration:none;font-size:11px}
.nav a.home{left:28px;width:132px;text-align:center;font-weight:600;font-size:12px}
.nav a.about{left:198px}
.nav a.how{left:334px}
/* hero */
.hero{position:absolute;left:0;top:76px;width:932px;height:324px;background:radial-gradient(ellipse at 50% 40%,#4a3a2c 0%,#2e241c 60%,#1f1914 100%)}
.hero h1{position:absolute;top:92px;width:100%;text-align:center;color:#fff;font-size:28px;font-weight:600}
.hero p{position:absolute;top:145px;width:100%;text-align:center;color:#fff;font-size:19px}
.select{position:absolute;left:213px;top:204px;width:368px;height:32px;background:#fff;font-size:10px;color:#555;line-height:32px;padding-left:11px}
.select svg{position:absolute;right:12px;top:13px}
.search{position:absolute;left:596px;top:204px;width:128px;height:32px;background:var(--blue);color:#fff;font-size:12px;font-weight:600;text-align:center;line-height:32px}
.hero .arrow{position:absolute;top:138px}
/* categories */
.cats{position:absolute;left:0;top:400px;width:932px;height:92px;display:flex}
.cat{flex:1;display:flex;flex-direction:column;align-items:center;justify-content:flex-end;padding-bottom:14px;gap:10px;color:#fff;font-size:13.5px;font-weight:600}
.cat svg{width:40px;height:38px}
.c-green{background:var(--green)}.c-blue{background:var(--blue)}.c-orange{background:var(--orange)}.c-yellow{background:var(--yellow)}
/* partners */
.partners{position:absolute;left:0;top:492px;width:932px;height:125px;border-bottom:1px solid #eee}
.bank{position:absolute;top:32px;width:146px;height:65px;border:1px solid #e2e2e2;display:flex;align-items:center;justify-content:center;gap:6px;font-size:15px;font-weight:600;color:#8a1538}
.bank i{width:14px;height:14px;background:currentColor;display:block}
/* steps */
.art{position:absolute;left:76px;top:637px;width:313px;height:224px;background:linear-gradient(160deg,#f2c98a,#7a1d35 70%,#e9e2d2)}
.divider{position:absolute;left:461px;top:655px;width:1px;height:200px;background:#e4e4e4}
.steps h2{position:absolute;left:521px;top:644px;font-size:21px;font-weight:400;color:var(--green)}
.step{position:absolute;left:524px;display:flex;align-items:center;gap:14px;font-size:11px;color:#444}
.step span.dash{margin-left:2px}
.apply{position:absolute;left:526px;top:828px;width:100px;height:32px;background:var(--blue);color:#fff;font-size:15px;text-align:center;line-height:32px;border-radius:2px}
/* features */
.features{position:absolute;left:0;top:897px;width:932px;height:54px;background:var(--green);color:#fff;font-size:12px;font-weight:600}
.feat{position:absolute;top:12px;display:flex;align-items:center;gap:14px;height:30px}
/* footer */
.footer{position:absolute;left:0;top:951px;width:932px;height:193px;background:var(--foot);color:#fff}
.col{position:absolute;top:28px}
.col h3{font-size:13px;font-weight:400;margin-bottom:12px}
.col li{list-style:none;font-size:10px;margin-bottom:9px}
.col li::before{content:"» ";margin-right:4px}
.contact p{font-size:10px;display:flex;gap:10px;margin-bottom:12px;line-height:1.7}
.social{display:flex;gap:10px;margin-top:6px}
.social i{width:28px;height:28px;border:2px solid #fff;border-radius:50%;display:block}
.email{margin-top:20px;width:132px;height:26px;background:#fff;color:#999;font-size:10px;line-height:26px;padding-left:9px;position:relative}
.email::after{content:"»";position:absolute;right:9px;color:#666}
.bottom{position:absolute;left:0;top:1144px;width:932px;height:56px;background:var(--foot-dark);color:#fff;font-size:10px;text-align:center;line-height:56px}
</style>
</head>
<body>
<header class="site-header">
  <div class="brand"><span class="brand-mark"></span>CredVista</div>
  <div class="quick">
    <svg width="8" height="12" viewBox="0 0 8 12"><rect x="0.5" y="0.5" width="7" height="11" rx="1.5" fill="none" stroke="#1a7fd0"/><circle cx="4" cy="9.5" r=".8" fill="#1a7fd0"/></svg>
    <b>– Quick Contact –</b> (555) 014 - 2290
  </div>
  <nav class="nav">
    <span class="nav-active"></span>
    <a class="home" href="#">Home</a>
    <a class="about" href="#">About us</a>
    <a class="how" href="#">How it works</a>
    <svg class="abs" style="left:461px;top:14px" width="13" height="13" viewBox="0 0 13 13"><circle cx="5.5" cy="5.5" r="4.2" fill="none" stroke="#fff" stroke-width="2"/><line x1="8.5" y1="8.5" x2="12" y2="12" stroke="#fff" stroke-width="2"/></svg>
  </nav>
</header>

<section class="hero" role="img" aria-label="Dark desk photo with charts, coins and hands">
  <svg class="arrow" style="left:33px" width="10" height="14"><path d="M8 1 2 7l6 6" fill="none" stroke="#fff" stroke-width="2"/></svg>
  <svg class="arrow" style="left:884px" width="10" height="14"><path d="M2 1l6 6-6 6" fill="none" stroke="#fff" stroke-width="2"/></svg>
  <h1>Match Your Loan In Less Than a Minute</h1>
  <p>We will help you get best interest rate</p>
  <div class="select">I would like to select a Product
    <svg width="8" height="5"><path d="M1 1l3 3 3-3" fill="none" stroke="#666"/></svg></div>
  <div class="search">Search Here</div>
</section>

<section class="cats">
  <div class="cat c-green"><svg viewBox="0 0 40 38"><path d="M4 20 20 5l16 15" fill="none" stroke="#fff" stroke-width="3"/><path d="M9 18v17h9v-9h5v9h9V18" fill="#fff"/></svg>Home Loan</div>
  <div class="cat c-blue"><svg viewBox="0 0 40 38"><path d="M3 19 20 4l17 15h-4v17H7V19z" fill="#fff"/><text x="20" y="30" text-anchor="middle" font-size="17" font-weight="600" fill="#34a7d7" font-family="Open Sans,sans-serif">$</text></svg>Loan Against Property</div>
  <div class="cat c-orange"><svg viewBox="0 0 40 38"><path d="M3 14l10-8 8 5 6-4 10 8-14 14-6-3z" fill="none" stroke="#fff" stroke-width="2.2"/></svg>Business Loan</div>
  <div class="cat c-yellow"><svg viewBox="0 0 40 38"><circle cx="20" cy="12" r="7" fill="none" stroke="#fff" stroke-width="2.2"/><path d="M6 36c0-9 6-14 14-14s14 5 14 14z" fill="none" stroke="#fff" stroke-width="2.2"/></svg>Personal Loan</div>
  <div class="cat c-green"><svg viewBox="0 0 40 38"><rect x="12" y="2" width="15" height="26" rx="2" fill="none" stroke="#fff" stroke-width="2.2"/><circle cx="19.5" cy="14" r="4" fill="#fff"/><path d="M22 22l8 4v10H20" fill="none" stroke="#fff" stroke-width="2.2"/></svg>Refinance</div>
</section>

<section class="partners">
  <svg class="abs" style="left:34px;top:50px" width="14" height="26"><path d="M13 1 1 13l12 12" fill="none" stroke="#bbb"/></svg>
  <div class="bank" style="left:76px"><i></i>Arcline Bank</div>
  <div class="bank" style="left:235px;color:#1e3f7a"><i></i>Meridia Bank</div>
  <div class="bank" style="left:393px;color:#1c2b6b"><i></i>Rowan Bank</div>
  <div class="bank" style="left:551px"><i></i>Indrava Bank</div>
  <div class="bank" style="left:709px;color:#d2232a"><i style="border-radius:50%;background:#1c2b6b"></i>Kestrel Bank</div>
  <svg class="abs" style="left:884px;top:50px" width="14" height="26"><path d="M1 1l12 12L1 25" fill="none" stroke="#bbb"/></svg>
</section>

<section class="steps">
  <div class="art" role="img" aria-label="Illustration of a customer at a laptop and an advisor holding a form"></div>
  <div class="divider"></div>
  <h2>CredVista Next Steps</h2>
  <div class="step" style="top:696px"><svg width="26" height="24"><rect x="1" y="3" width="18" height="20" fill="none" stroke="#555" stroke-width="1.5"/><path d="M5 9h10M5 13h10M5 17h7M16 16 25 2" stroke="#555" stroke-width="1.5"/></svg><span class="dash">-</span>Fill up the form</div>
  <div class="step" style="top:738px"><svg width="26" height="26"><circle cx="13" cy="13" r="11" fill="none" stroke="#555" stroke-width="1.5"/><path d="M3 13a10 10 0 0 1 20 0" fill="none" stroke="#555" stroke-width="3"/></svg><span class="dash">-</span>Get A Call From our customer friendly staff</div>
  <div class="step" style="top:780px"><svg width="26" height="24"><circle cx="7" cy="6" r="4" fill="none" stroke="#555" stroke-width="1.5"/><circle cx="19" cy="18" r="4" fill="none" stroke="#555" stroke-width="1.5"/><path d="M21 2 5 22" stroke="#555" stroke-width="1.5"/></svg><span class="dash">-</span>Get Matched for lowest interest rates</div>
  <div class="apply">Apply Now</div>
</section>

<section class="features">
  <div class="feat" style="left:76px"><svg width="30" height="30"><circle cx="15" cy="15" r="12" fill="none" stroke="#fff" stroke-width="1.8" stroke-dasharray="4 2"/><path d="M10 20 20 10" stroke="#fff" stroke-width="1.8"/><circle cx="11" cy="11" r="2" fill="#fff"/><circle cx="19" cy="19" r="2" fill="#fff"/></svg>Lowest Interest Rates</div>
  <div class="feat" style="left:289px"><svg width="30" height="30"><circle cx="15" cy="15" r="12" fill="none" stroke="#fff" stroke-width="1.8"/><path d="M15 8v7h5" fill="none" stroke="#fff" stroke-width="1.8"/></svg>Quick Approvals</div>
  <div class="feat" style="left:470px"><svg width="26" height="30"><circle cx="13" cy="9" r="6" fill="#fff"/><path d="M1 29c0-8 5-12 12-12s12 4 12 12z" fill="#fff"/></svg>Door Step Service</div>
  <div class="feat" style="left:656px"><svg width="30" height="30"><path d="M15 2 27 7v8c0 7-6 12-12 14C9 27 3 22 3 15V7z" fill="none" stroke="#fff" stroke-width="1.8"/><circle cx="15" cy="13" r="3" fill="#fff"/><path d="M9 22c1-4 3-5 6-5s5 1 6 5" fill="#fff"/></svg>Customer Centric Approach</div>
</section>

<footer class="footer">
  <div class="col" style="left:75px"><h3>Home loan</h3><ul><li>Meridia Loan</li><li>Sunbay Loan</li><li>Harbor Loan</li><li>Arcline Loan</li><li>Cityline Loan</li></ul></div>
  <div class="col" style="left:189px"><h3>Personal loan</h3><ul><li>Meridia Loan</li><li>Sunbay Loan</li><li>Harbor Loan</li><li>Arcline Loan</li><li>Cityline Loan</li></ul></div>
  <div class="col" style="left:307px"><h3>Property loan</h3><ul><li>Meridia Loan</li><li>Sunbay Loan</li><li>Harbor Loan</li><li>Arcline Loan</li><li>Cityline Loan</li></ul></div>
  <div class="col" style="left:421px"><h3>Business loan</h3><ul><li>Meridia Loan</li><li>Sunbay Loan</li><li>Harbor Loan</li><li>Arcline Loan</li><li>Cityline Loan</li></ul></div>
  <div class="col contact" style="left:540px;width:160px"><h3>Contact us</h3>
    <p><svg width="13" height="11" style="flex:none;margin-top:4px"><path d="M1 6 6.5 1 12 6v5H1z" fill="#fff"/></svg>2207 W. Linden Ct. | Maple Grove KS 60412</p>
    <p><svg width="13" height="13" style="flex:none;margin-top:3px"><rect x="3" y="1" width="7" height="11" rx="1" fill="none" stroke="#fff" stroke-width="1.4"/></svg>Call Us : (555)014-2290</p>
    <p><svg width="13" height="11" style="flex:none;margin-top:4px"><rect x="0.7" y="0.7" width="11.6" height="9" fill="none" stroke="#fff" stroke-width="1.2"/><path d="M1 1l5.5 5L12 1" fill="none" stroke="#fff" stroke-width="1.2"/></svg>hello@credvista.in</p>
  </div>
  <div class="col" style="left:716px"><h3>Connect us with</h3>
    <div class="social"><i></i><i></i><i></i><i></i></div>
    <div class="email">Email</div>
  </div>
</footer>
<div class="bottom">© CredVista 2016 . All Rights Reserved</div>
</body>
</html>
```